Tallowreed Advisory Partners Business Card Design

We have the logo we just need someone to design a modern business card design.

Name: Desmond Munkalt
Phone: 3055550148
Mobile: 9175550193
Web:www.tallowreedadvisory.example
email: dmunkalt@tallowreedadvisory.example
Company: Tallowreed Advisory Partners
Title: CEO

Address: 718 Quillmore Ave, Miami, Florida 33190

Target Market(s)

companies over 100 employees

Industry/Entity Type

Business

```html
<!DOCTYPE html>
<html lang="en">
<head>
<meta charset="utf-8">
<title>Tallowreed Advisory Partners — Business Card</title>
<link href="https://fonts.googleapis.com/css2?family=Arimo:wght@400;700&display=swap" rel="stylesheet">
<style>
  :root {
    --card-dark: #272526;
    --brand-blue: #335cff;
    --text-white: #ffffff;
    --page-bg: #ffffff;
  }
  * { margin: 0; padding: 0; box-sizing: border-box; }
  html, body { width: 1200px; height: 1000px; overflow: hidden; background: var(--page-bg); }
  body { position: relative; font-family: "Arimo", Arial, sans-serif; }

  .card { position: absolute; background: var(--card-dark); }
  .card--flat { left: 197px; top: 50px; width: 831px; height: 488px; }
  .card--tent { left: 197px; top: 708px; width: 833px; height: 244px; }

  .tent-tab {
    position: absolute;
    left: 317px; top: 592px;
    width: 170px; height: 170px;
    border-radius: 50%;
    background: var(--card-dark);
  }

  .brand-mark {
    position: absolute;
    width: 132px; height: 132px;
    border-radius: 50%;
    background: var(--brand-blue);
  }
  .card--flat .brand-mark { left: 138px; top: 147px; }
  .tent-tab .brand-mark { left: 19px; top: 19px; }

  .brand-name {
    position: absolute;
    left: 36px;
    width: 339px;
    text-align: center;
    font-weight: 700;
    font-size: 42px;
    letter-spacing: 1px;
    color: var(--text-white);
    line-height: 1;
    white-space: nowrap;
  }
  .card--flat .brand-name { top: 306px; }
  .card--tent .brand-name { top: 52px; }

  .person {
    position: absolute;
    right: 43px;
    text-align: right;
    line-height: 1;
    white-space: nowrap;
  }
  .card--flat .person { top: 304px; }
  .card--tent .person { top: 50px; }
  .person-name { font-size: 32px; color: var(--brand-blue); font-weight: 400; }
  .person-title { font-size: 30px; color: var(--text-white); margin-top: 8px; }

  .contact {
    position: absolute;
    left: 0; width: 100%;
    text-align: center;
    font-size: 22px;
    color: var(--text-white);
    line-height: 30px;
    white-space: nowrap;
  }
  .card--flat .contact { top: 388px; }
  .card--tent .contact { top: 134px; }
</style>
</head>
<body>

  <section class="card card--flat">
    <div class="brand-mark"></div>
    <div class="brand-name">TALLOWREED</div>
    <div class="person">
      <div class="person-name">DESMOND MUNKALT</div>
      <div class="person-title">CEO</div>
    </div>
    <div class="contact">
      <div>Ph: (305) 555-0148&nbsp; | Cel: (917) 555-0193</div>
      <div>dmunkalt@tallowreedadvisory.example | www.tallowreedadvisory.example</div>
      <div>718 Quillmore Ave, Miami, Florida 33190</div>
    </div>
  </section>

  <div class="tent-tab">
    <div class="brand-mark"></div>
  </div>
  <section class="card card--tent">
    <div class="brand-name">TALLOWREED</div>
    <div class="person">
      <div class="person-name">DESMOND MUNKALT</div>
      <div class="person-title">CEO</div>
    </div>
    <div class="contact">
      <div>Ph: (305) 555-0148&nbsp; | Cel: (917) 555-0193</div>
      <div>dmunkalt@tallowreedadvisory.example | www.tallowreedadvisory.example</div>
      <div>718 Quillmore Ave, Miami, Florida 33190</div>
    </div>
  </section>

</body>
</html>
```